Business Card Design Project

We need a business card design for a new company based in Singapore called 'Bright Harbor Pte Ltd'. We provide personal development training and emotional intelligence workshops. Our slogan is "Discover your true strengths". We will not have a company address on the business card. Only phone number, email address and website address.

Target Market(s)

Adults age 25 to 45 years old.
Mostly working in a job.

Industry/Entity Type

Training

Colors
0255a2
f37123

```html
<!DOCTYPE html>
<html lang="en">
<head>
<meta charset="utf-8">
<title>Bright Harbor Pte Ltd – Business Card</title>
<link rel="stylesheet" href="https://fonts.googleapis.com/css2?family=Montserrat:wght@500;700;800&family=Libre+Baskerville:wght@400;700&display=swap">
<style>
  :root {
    --brand-blue: #0255a2;
    --brand-navy: #1b2a5c;
    --brand-orange: #f37123;
    --card-white: #ffffff;
    --page-bg: #e9e7e3;
    --rule-grey: #8a8f99;
  }
  * { box-sizing: border-box; margin: 0; padding: 0; }
  html, body {
    width: 1200px; height: 900px; overflow: hidden;
    background: var(--page-bg);
  }
  .canvas {
    width: 1200px; height: 900px;
    display: flex; flex-direction: column; align-items: center; justify-content: center;
    gap: 40px;
  }
  .card {
    position: relative;
    width: 682px; height: 390px;
    overflow: hidden;
    box-shadow: 0 10px 28px rgba(0,0,0,0.18);
  }

  /* Front */
  .card--front { background: var(--brand-orange); }
  .front-lockup {
    position: absolute; left: 70px; top: 120px;
    display: flex; align-items: center; gap: 26px;
  }
  .front-mark {
    width: 140px; height: 140px; border-radius: 50%;
    border: 9px solid var(--card-white);
  }
  .front-text { display: flex; flex-direction: column; }
  .front-name {
    font-family: "Montserrat", sans-serif; font-weight: 800;
    font-size: 40px; line-height: 1.05; color: var(--brand-navy);
    letter-spacing: -0.5px;
  }
  .front-rule {
    width: 250px; height: 2px; background: var(--brand-navy);
    margin: 12px 0 14px;
  }
  .front-slogan {
    font-family: "Montserrat", sans-serif; font-weight: 700;
    font-size: 20px; color: var(--card-white); letter-spacing: 0.3px;
    align-self: flex-end;
  }

  /* Back */
  .card--back { background: var(--card-white); }
  .back-lockup {
    position: absolute; left: 34px; top: 64px;
    display: flex; align-items: center; gap: 16px;
  }
  .back-mark {
    width: 96px; height: 96px; border-radius: 50%;
    border: 8px solid var(--brand-navy);
  }
  .back-name {
    font-family: "Montserrat", sans-serif; font-weight: 800;
    font-size: 24px; line-height: 1.1; color: var(--brand-navy);
    letter-spacing: -0.3px;
  }
  .back-name-rule { width: 140px; height: 1.5px; background: var(--rule-grey); margin-top: 8px; }

  .person {
    position: absolute; right: 40px; top: 56px; text-align: right;
    font-family: "Libre Baskerville", serif; font-weight: 700;
  }
  .person-name { font-size: 22px; color: var(--brand-orange); letter-spacing: 0.5px; }
  .person-title { font-size: 13px; color: var(--brand-blue); letter-spacing: 0.5px; margin-top: 2px; }
  .person-rule {
    position: absolute; right: 34px; top: 112px;
    width: 280px; height: 2px; background: var(--brand-blue);
  }
  .website {
    position: absolute; right: 40px; top: 140px;
    display: flex; align-items: center; gap: 10px;
    font-family: "Libre Baskerville", serif; font-weight: 700;
    font-size: 16px; color: var(--brand-blue);
  }

  .contact-rule {
    position: absolute; left: 34px; top: 238px;
    width: 340px; height: 2px; background: var(--brand-blue);
  }
  .contacts {
    position: absolute; left: 40px; top: 256px;
    list-style: none;
    font-family: "Libre Baskerville", serif; font-weight: 700;
    font-size: 18px; color: var(--brand-blue);
  }
  .contacts li { display: flex; align-items: center; gap: 14px; line-height: 27px; }
  .icon { width: 16px; height: 16px; flex: none; }

  .band { position: absolute; bottom: 0; height: 22px; }
  .band--blue { left: 0; width: 64%; background: var(--brand-blue); }
  .band--orange { right: 0; width: 35%; background: var(--brand-orange); }
</style>
</head>
<body>
<main class="canvas">

  <section class="card card--front" aria-label="Business card front">
    <div class="front-lockup">
      <div class="front-mark"></div>
      <div class="front-text">
        <div class="front-name">Bright Harbor<br>Pte Ltd</div>
        <div class="front-rule"></div>
        <div class="front-slogan">Discover your true strengths</div>
      </div>
    </div>
  </section>

  <section class="card card--back" aria-label="Business card back">
    <div class="back-lockup">
      <div class="back-mark"></div>
      <div>
        <div class="back-name">Bright Harbor<br>Pte Ltd</div>
        <div class="back-name-rule"></div>
      </div>
    </div>

    <div class="person">
      <div class="person-name">DANIEL TAN</div>
      <div class="person-title">MANAGER</div>
    </div>
    <div class="person-rule"></div>

    <div class="website">
      <svg class="icon" viewBox="0 0 16 16" aria-hidden="true">
        <circle cx="9.5" cy="6.5" r="4.5" fill="none" stroke="var(--brand-orange)" stroke-width="2.2"/>
        <line x1="6" y1="10" x2="1.5" y2="14.5" stroke="var(--brand-orange)" stroke-width="2.6" stroke-linecap="round"/>
      </svg>
      <span>www.brightharborpteltd.com</span>
    </div>

    <div class="contact-rule"></div>
    <ul class="contacts">
      <li>
        <svg class="icon" viewBox="0 0 16 16" aria-hidden="true">
          <path d="M3 1.5 L6 1.5 L7 5 L5.2 6.4 C6 8.3 7.7 10 9.6 10.8 L11 9 L14.5 10 L14.5 13 C14.5 14 13.6 14.6 12.6 14.5 C6.8 13.8 2.2 9.2 1.5 3.4 C1.4 2.4 2 1.5 3 1.5 Z" fill="var(--brand-orange)"/>
        </svg>
        <span>+65 6123 4567</span>
      </li>
      <li>
        <svg class="icon" viewBox="0 0 16 16" aria-hidden="true">
          <rect x="4" y="1" width="8" height="14" rx="1.5" fill="var(--brand-orange)"/>
          <rect x="5.5" y="3" width="5" height="6" fill="var(--card-white)"/>
          <circle cx="8" cy="12.2" r="1" fill="var(--card-white)"/>
        </svg>
        <span>+65 9123 4567</span>
      </li>
      <li>
        <svg class="icon" viewBox="0 0 16 16" aria-hidden="true">
          <rect x="1" y="3.5" width="14" height="9.5" fill="var(--brand-orange)"/>
          <polyline points="1.5,4 8,9 14.5,4" fill="none" stroke="var(--card-white)" stroke-width="1.3"/>
        </svg>
        <span>danieltan@mail.com</span>
      </li>
    </ul>

    <div class="band band--blue"></div>
    <div class="band band--orange"></div>
  </section>

</main>
</body>
</html>
```